Employee Benefits Consulting Firm needs a refreshed website

I have a business (an employee benefits consulting firm) called KRV Benefits Group, LLC (www.krvbenefits-example.com).  The existing site is currently hosted on Nimbuspark.  The business has been pretty much dormant since 2012.  I've relaunched the business and need a new website and looking for the website to be in Wordpress and to start with just 5 pages:
Home
About Us
Services
Contact Us
Blog
Some information about KRV Benefits Group:
There is a tremendous waste (financial) in the traditional employee benefit model --- the current system is broken and simply stated, unsustainable. We take a very different approach when it comes to employee benefits consulting, constantly strive to provide short-term and long-term cost containment strategies that truly bend the healthcare cost curve... Many of our clients consider us as Benefit Architects...
Each employer/business is unique.
In short, our firm works with Employers to first understand their business.... -their history, their corporate structure, their leadership, their values, their uniqueness, etc.
Then we take a deep dive and get a strong grasp on their existing benefits program... -how did they get to where they are today, what are their goals/objectives, what is their risk tolerance, what are current pain points, are they compliant, etc.
Then after thorough analysis, we deliver a tailored solution. We implement the programs and manage the various aspects and moving parts of the program throughout the year.
We also are constantly analyzing the performance of the plan and monitor population health. We aggregate data and constantly refine the approach/strategy.

Updates
I made a few updates to the brief over the past couple of days...below is the updated brief:
Home
About Us
Services
Contact Us
Blog
MUST HAVE:
Mobile Friendly
PLEASE USE TORVEL THEME
SHOULD HAVE:
the ability to add embedded video client testimonials
the ability for online chat
SHOULD NOT HAVE:
Photos from the old/existing website, I apologize for the late directive

I apologize for the delay on responding. Content is just about complete and will submit ASAP. Please let me know your availability to complete this project.

Updated content has been posted to this project.  I appreciate everybody's patience as we are working through this!

Target Market(s)
This is a BtoB website, primarily focusing on the following targets: CFOs, CEOs, Directors of Human Resources
Industry/Entity Type
Consulting
Number of Pages Required
5+ page
Requirements
Must have
- Mobile Friendly
- PLEASE USE TORVEL THEME
Nice to have
- the ability to add embedded video client testimonials
- the ability for online chat
Should not have
- Photos from the old/existing website, I apologise for the late directive

```html
<!DOCTYPE html>
<html lang="en">
<head>
<meta charset="utf-8">
<title>KRV Benefits Group, LLC</title>
<link rel="stylesheet" href="https://fonts.googleapis.com/css2?family=Open+Sans:ital,wght@0,400;0,600;0,700;1,400&family=Roboto:wght@400;500&family=Montserrat:wght@600;700&display=swap">
<style>
:root{
  --brand:#4a67a6;
  --brand-dark:#3d5894;
  --accent:#c0323a;
  --ink:#333;
  --muted:#555;
  --paper:#f6f6f6;
  --green:#8db57a;
  --footer-base:#444;
  --sky:#36a9e1;
}
*{box-sizing:border-box;margin:0;padding:0}
html,body{width:679px;height:1200px;overflow:hidden}
body{position:relative;background:var(--paper);font-family:"Roboto",sans-serif;color:var(--ink)}
.abs{position:absolute}
.topbar{left:0;top:0;width:679px;height:27px;background:var(--brand)}
.social{top:9px;display:flex;gap:8px}
.social span{width:8px;height:8px;border-radius:50%;background:#c9d3ea;display:block}
.header{left:0;top:27px;width:679px;height:51px;background:#fff}
.logo-box{left:62px;top:0;width:108px;height:70px;background:#fff;display:flex;align-items:center;justify-content:center;gap:5px;z-index:2}
.logo-box .mark{width:10px;height:10px;background:var(--brand)}
.logo-box .name{font-family:"Open Sans",sans-serif;font-weight:700;font-size:13px;color:var(--brand);line-height:1.1}
.nav{top:43px;left:340px;width:290px;height:21px;font-family:"Open Sans",sans-serif;font-size:6.6px;color:#222;z-index:2}
.nav a{color:inherit;text-decoration:none;position:absolute;white-space:nowrap;top:0;line-height:21px}
.nav .active{background:var(--brand);color:#fff;border-radius:2px;width:51px;height:21px;text-align:center}
.hero{left:0;top:78px;width:679px;height:218px;background:radial-gradient(circle at 80% 40%,#3a4f73 0%,#1a2a44 35%,#0d1626 75%)}
.hero-text{left:40px;top:148px;width:356px;text-align:center;color:#fff;font-family:"Open Sans",sans-serif}
.hero-text .kicker{font-style:italic;font-size:23px;line-height:1}
.hero-text .title{font-weight:700;font-size:31px;line-height:1.05;letter-spacing:-.3px}
.hero-text .sub{font-size:16px;margin-top:2px}
.hero-photo{left:505px;top:120px;width:132px;height:130px;border-radius:8px;background:radial-gradient(ellipse at 50% 55%,#6f95b8 0%,#2b4160 60%,transparent 100%)}
.plus{left:628px;top:80px;width:51px;height:48px;background:#151d2b;display:flex;align-items:center;justify-content:center}
.welcome-title{left:0;top:331px;width:679px;text-align:center;font-family:"Open Sans",sans-serif;font-weight:600;font-size:19px;color:var(--brand)}
.rule{height:1.5px;background:var(--accent)}
.welcome-copy{left:62px;top:386px;width:555px;text-align:center;font-size:9.9px;line-height:1.3;color:var(--muted)}
.btn-more{width:34px;height:16px;border:1px solid var(--accent);font-size:7.5px;text-align:center;line-height:14px;color:#5a78b3}
.services{left:0;top:494px;width:679px;height:226px;background:linear-gradient(135deg,#6a80b0 0%,#5870a4 45%,#4a6498 100%)}
.services-title{left:0;top:24px;width:679px;text-align:center;color:#fff;font-family:"Open Sans",sans-serif;font-size:19px;font-weight:600}
.svc{top:84px;width:160px;text-align:center;color:#fff}
.svc h3{font-family:"Open Sans",sans-serif;font-weight:600;font-size:9.6px;line-height:1.1;height:30px}
.svc p{font-size:7.6px;line-height:1.25;color:#e6ebf5}
.svc .btn-more{position:absolute;left:63px;top:78px;color:#fff;border-color:var(--accent)}
.section-head{font-family:"Open Sans",sans-serif;font-weight:700;font-size:15px;color:var(--brand)}
.arrows{display:flex;gap:2px}
.arrows span{width:10px;height:10px;border-radius:50%;background:var(--brand);display:flex;align-items:center;justify-content:center}
.divider{height:1px;background:#bbb}
.post{left:65px;width:251px;height:42px}
.thumb{position:absolute;left:0;top:0;width:40px;height:41px;border:1px solid #999;background:linear-gradient(135deg,#8a6f5e,#4b6a8e)}
.post h4{position:absolute;left:49px;top:3px;font-family:"Open Sans",sans-serif;font-weight:700;font-size:8.8px;color:#333}
.post p{position:absolute;left:49px;top:16px;width:202px;font-size:7.2px;line-height:1.25;color:#555;text-align:justify}
.post time{position:absolute;left:49px;top:36px;font-size:7px;color:#333}
.field{left:362px;width:252px;border:1px solid #aaa;background:#fff;font-family:"Open Sans",sans-serif;font-size:7px;color:#666;padding:5px 8px}
.submit{left:362px;top:894px;width:51px;height:19px;background:var(--brand);color:#fff;font-size:7.2px;text-align:center;line-height:19px}
.newsletter{left:0;top:942px;width:679px;height:38px;background:var(--green)}
.news-icon{left:109px;top:8px;width:22px;height:22px;border-radius:50%;background:#fff;display:flex;align-items:center;justify-content:center}
.news-label{left:140px;top:9px;font-family:"Open Sans",sans-serif;font-size:14px;color:#fff}
.news-input{left:286px;top:10px;width:212px;height:17px;background:#fff;font-size:7px;color:#333;padding:4px 8px;font-family:"Open Sans",sans-serif}
.subscribe{left:504px;top:10px;width:70px;height:17px;background:var(--brand);color:#fff;font-size:7.5px;font-weight:500;text-align:center;line-height:17px}
.footer{left:0;top:980px;width:679px;height:178px;background:var(--brand);color:#fff}
.foot-logo{left:72px;top:42px;display:flex;align-items:center;gap:4px;font-family:"Open Sans",sans-serif;font-weight:700;font-size:11px}
.foot-logo span{width:8px;height:8px;background:#fff}
.foot-about{left:72px;top:85px;width:104px;font-size:6.8px;line-height:1.4;color:#e1e7f3}
.vline{top:42px;width:1px;height:104px;background:#fff}
.foot-head{font-family:"Montserrat",sans-serif;font-weight:600;font-size:9.4px;letter-spacing:.2px}
.foot-head em{font-style:normal;color:var(--sky)}
.dots{height:0;border-top:1px dotted #c9d3ea}
.links{left:218px;top:66px;font-size:7.6px;line-height:18px;list-style:none}
.contact-line{left:330px;display:flex;gap:7px;font-size:7.4px;line-height:1.3}
.contact-line svg{flex:none;margin-top:1px}
.foot-social{left:490px;top:70px;display:flex;gap:11px}
.foot-social span{width:6px;height:6px;border-radius:50%;background:#fff}
.call{left:490px;top:110px;font-family:"Montserrat",sans-serif;font-weight:600;font-size:9px}
.call strong{display:block;font-weight:700;font-size:11px;margin-top:2px;letter-spacing:.3px}
.copyright{left:0;top:1158px;width:679px;height:42px;background:var(--footer-base);color:#ddd;font-size:6.6px;text-align:center;line-height:42px}
</style>
</head>
<body>

<div class="abs topbar"></div>
<div class="abs social" style="left:522px"><span></span><span></span><span></span><span></span><span></span></div>

<header class="abs header"></header>
<nav class="abs nav">
  <a style="left:12px">HOME</a>
  <a class="active" style="left:50px">ABOUT US</a>
  <a style="left:119px">SERVICES</a>
  <a style="left:175px">CONTACTS US</a>
  <a style="left:246px">OUR BLOG</a>
</nav>
<div class="abs logo-box"><span class="mark"></span><span class="name">KRV Benefits<br>Group, LLC</span></div>

<section class="abs hero" role="img" aria-label="Photo of open hands holding small figures of a team, bokeh lights behind"></section>
<div class="abs hero-photo" role="img" aria-label="Hands holding a group of people figurines"></div>
<div class="abs hero-text">
  <div class="kicker">THE BENEFIT OF</div>
  <div class="title">INNOVATIVE THINING</div>
  <div class="sub">Employee Benefits Consulting</div>
</div>
<div class="abs plus"><svg width="20" height="20" viewBox="0 0 20 20"><path d="M10 1v18M1 10h18" stroke="#fff" stroke-width="2"/></svg></div>

<h1 class="abs welcome-title">Welcome to KRV Benefits Group, LLC</h1>
<div class="abs rule" style="left:316px;top:368px;width:58px"></div>
<p class="abs welcome-copy">At KRV we fully understand the correlation between benefits satisfaction and job satisfaction.&nbsp; A proper benefits plan has the potential to influence so many lives in hundreds of positive ways therefore we strive to help make your employees healthier and happier at work.&nbsp; If you have been asked, “How can we do more without spending much more?”, then it is time to visit with KRV Benefits Group.</p>
<div class="abs btn-more" style="left:328px;top:454px">more</div>

<section class="abs services" role="img" aria-label="Blue-tinted photo of team hands stacked together">
  <h2 class="abs services-title">Our Services</h2>
  <div class="abs rule" style="left:312px;top:57px;width:57px"></div>
  <div class="abs svc" style="left:64px">
    <h3>Benchmark Your<br>Current Benefits Program</h3>
    <p>Lorem ipsum dolor sit amet, consectetur adipiscing elit, sed do eiusmod tempor incididunt ut labore et dolore magna aliqua. Ut enim ad minim veniam, quis</p>
    <div class="btn-more">more</div>
  </div>
  <div class="abs svc" style="left:240px;width:194px">
    <h3>Technology<br>Complete Online Benefits Administration</h3>
    <p style="padding:0 17px">Lorem ipsum dolor sit amet, consectetur adipiscing elit, sed do eiusmod tempor incididunt ut labore et dolore magna aliqua. Ut enim ad minim veniam, quis</p>
    <div class="btn-more" style="left:80px">more</div>
  </div>
  <div class="abs svc" style="left:446px">
    <h3>Technology<br>Custom Employee Portals</h3>
    <p>Lorem ipsum dolor sit amet, consectetur adipiscing elit, sed do eiusmod tempor incididunt ut labore et dolore magna aliqua. Ut enim ad minim veniam, quis</p>
    <div class="btn-more">more</div>
  </div>
</section>

<h2 class="abs section-head" style="left:62px;top:750px">Latest Blog</h2>
<div class="abs arrows" style="left:287px;top:757px"><span><svg width="6" height="6" viewBox="0 0 6 6"><path d="M4 1L2 3l2 2" stroke="#fff" stroke-width="1.3" fill="none"/></svg></span><span><svg width="6" height="6" viewBox="0 0 6 6"><path d="M2 1l2 2-2 2" stroke="#fff" stroke-width="1.3" fill="none"/></svg></span></div>
<div class="abs divider" style="left:62px;top:782px;width:254px"></div>

<article class="abs post" style="top:801px">
  <div class="thumb" role="img" aria-label="Blog thumbnail: business handshake"></div>
  <h4>Verum tamen cum de rebus</h4>
  <p>Lorem ipsum dolor sit amet, consectetur adipiscing elit. Quid utem habent admirationis,</p>
  <time>10-Oct 2017</time>
</article>
<article class="abs post" style="top:862px">
  <div class="thumb" role="img" aria-label="Blog thumbnail: colleague at the office"></div>
  <h4>Verum tamen cum de rebus</h4>
  <p>Lorem ipsum dolor sit amet, consectetur adipiscing elit. Quid utem habent admirationis,</p>
  <time>10-Oct 2017</time>
</article>

<h2 class="abs section-head" style="left:359px;top:750px">Contact us</h2>
<div class="abs arrows" style="left:583px;top:757px"><span><svg width="6" height="6" viewBox="0 0 6 6"><path d="M4 1L2 3l2 2" stroke="#fff" stroke-width="1.3" fill="none"/></svg></span><span><svg width="6" height="6" viewBox="0 0 6 6"><path d="M2 1l2 2-2 2" stroke="#fff" stroke-width="1.3" fill="none"/></svg></span></div>
<div class="abs divider" style="left:359px;top:782px;width:253px"></div>
<div class="abs field" style="top:796px;height:20px">Your Name</div>
<div class="abs field" style="top:819px;height:20px">Your Email</div>
<div class="abs field" style="top:842px;height:49px">Message</div>
<div class="abs submit">Submit</div>

<section class="abs newsletter">
  <div class="abs news-icon"><svg width="12" height="12" viewBox="0 0 12 12"><circle cx="6" cy="6" r="6" fill="var(--brand)"/><rect x="3" y="4" width="6" height="4.3" fill="#fff"/><path d="M3 4l3 2.3L9 4" stroke="var(--brand)" stroke-width=".7" fill="none"/></svg></div>
  <div class="abs news-label">News letter Signup</div>
  <div class="abs news-input">Enter Your Email</div>
  <div class="abs subscribe">SUBSCRIBE</div>
</section>

<footer class="abs footer">
  <div class="abs foot-logo"><span></span>KRV Benefits</div>
  <p class="abs foot-about">Lorem ipsum dolor sit amet, consectetur adipiscing elit. Morbi auctor ullamcorper congue. Phasellus quis lacus quis ante ornare tincidunt lobortis quisenim.</p>
  <div class="abs vline" style="left:194px"></div>

  <div class="abs foot-head" style="left:218px;top:42px">QUICK LINKS</div>
  <div class="abs dots" style="left:218px;top:58px;width:80px"></div>
  <ul class="abs links"><li>&gt; Home</li><li>&gt; About Us</li><li>&gt; Sevices</li><li>&gt; Blog</li><li>&gt; Contact Us</li></ul>
  <div class="abs vline" style="left:305px"></div>

  <div class="abs foot-head" style="left:329px;top:42px">CONTACT US</div>
  <div class="abs dots" style="left:329px;top:58px;width:106px"></div>
  <div class="abs contact-line" style="top:70px"><svg width="8" height="10" viewBox="0 0 8 10"><path d="M4 10S0 5.5 0 4a4 4 0 018 0c0 1.5-4 6-4 6z" fill="#fff"/><circle cx="4" cy="4" r="1.5" fill="var(--brand)"/></svg><span>4820 Larkmoor Parkway,<br>Suite 210 Dallas,<br>Texas 75200<br>Click here for directions</span></div>
  <div class="abs contact-line" style="top:112px"><svg width="8" height="8" viewBox="0 0 8 8"><path d="M1 .5l1.8 0 .7 1.8-1 .8a4.5 4.5 0 002.4 2.4l.8-1 1.8.7V7c0 .5-.5 1-1 1A7 7 0 010 1.5C0 1 .5.5 1 .5z" fill="#fff"/></svg><span>(800) 555-0142</span></div>
  <div class="abs contact-line" style="top:125px"><svg width="8" height="8" viewBox="0 0 8 8"><path d="M1 .5l1.8 0 .7 1.8-1 .8a4.5 4.5 0 002.4 2.4l.8-1 1.8.7V7c0 .5-.5 1-1 1A7 7 0 010 1.5C0 1 .5.5 1 .5z" fill="#fff"/></svg><span>(972) 555-0187</span></div>
  <div class="abs contact-line" style="top:138px"><svg width="8" height="7" viewBox="0 0 8 7"><rect width="8" height="6" y=".5" fill="#fff"/><path d="M0 .8l4 3 4-3" stroke="var(--brand)" stroke-width=".8" fill="none"/></svg><span>info@krvbenefits-example.com</span></div>
  <div class="abs vline" style="left:454px"></div>

  <div class="abs foot-head" style="left:486px;top:40px">FOLLOW US <em>ON</em></div>
  <div class="abs dots" style="left:486px;top:56px;width:105px"></div>
  <div class="abs foot-social"><span></span><span></span><span></span><span></span></div>
  <div class="abs" style="left:490px;top:92px;width:10px;height:1px;background:#fff"></div>
  <div class="abs call">CALL US ON<strong>555-010-4477</strong></div>
</footer>

<div class="abs copyright">Copyright © 2017 Halvern Studio - All Rights Reserved</div>

</body>
</html>
```